Industrial/Commercial Plumbing Capability Statement

Would like a construction capability statement/Brochure amended to be similar to the attached. -
Have included photos and Notes on the attached
would like project photos to be used
This is a previous capability statement that we would like amended and altered to include, safety, QA and Recent Projects
Please use our company logo
Updates

Need extra days to review

Target Market(s)

Construction work - Industrial

Industry/Entity Type

Plumbing

Requirements
Must have
• Include all items in contents page

Eye Catching Photos relevant to construction industry and relevant to topic on page

```html
<!DOCTYPE html>
<html lang="en">
<head>
<meta charset="utf-8">
<title>Ridgeline Plumbers – Capability Statement</title>
<link href="https://fonts.googleapis.com/css2?family=Barlow:wght@400;500;700;800&display=swap" rel="stylesheet">
<style>
:root{
  --navy:#0f3a62;
  --navy-deep:#0b2f52;
  --white:#ffffff;
  --bg-light:#e7e8e9;
  --bg-dark:#c8c9cb;
  --sky:#7d95c2;
  --sunset:#e9894a;
  --foliage:#3a4424;
}
*{box-sizing:border-box;margin:0;padding:0}
html,body{width:1200px;height:1146px;overflow:hidden}
body{position:relative;background:var(--bg-light);font-family:"Barlow",Arial,sans-serif;color:var(--white)}
.backdrop{position:absolute;inset:0;width:1200px;height:1146px}
.page{position:absolute;width:328px;height:463px;background:var(--navy);overflow:hidden;box-shadow:2px 3px 6px rgba(0,0,0,.28)}
.col-1{left:82px}.col-2{left:436px}.col-3{left:790px}
.row-1{top:101px}.row-2{top:582px}
.page-title{position:absolute;left:27px;border-left:2px solid var(--white);padding-left:7px;font-weight:800;font-size:21px;line-height:1.12;letter-spacing:.2px;text-transform:uppercase}
.brand{position:absolute;right:20px;bottom:32px;display:flex;align-items:center;gap:4px;font-weight:800;font-size:11.5px;letter-spacing:.2px;color:var(--white)}
.brand-square{width:9px;height:9px;background:var(--white)}
.body-text{font-size:5.6px;line-height:1.42;font-weight:400}
.body-text p{margin-bottom:6px}

/* cover */
.cover-photo{position:absolute;inset:0;background:linear-gradient(180deg,#6f8fc9 0%,#9aa4c8 22%,#d9a08a 42%,var(--sunset) 55%,#8a7a66 68%,#4d5638 80%,var(--foliage) 100%)}
.cover .page-title{top:43px}

/* contents */
.contents .page-title{top:40px;left:42px}
.toc{position:absolute;left:54px;top:175px;width:217px;list-style:none}
.toc li{display:flex;align-items:baseline;font-weight:700;font-size:7.6px;height:14.7px;text-transform:uppercase}
.toc .dots{flex:1;border-bottom:1px dotted var(--white);margin:0 2px;transform:translateY(-2px)}

/* introduction */
.intro .page-title{top:52px}
.intro .body-text{position:absolute;left:27px;top:102px;width:274px}
.intro .body-text p{margin-bottom:7px}
.callout{background:var(--white);color:var(--navy-deep);font-size:8px;font-weight:500;text-align:center;line-height:1.35;padding:7px 6px;margin:10px -7px 11px}

/* about */
.about .page-title{top:40px}
.about-cols{position:absolute;left:27px;top:114px;width:275px;display:flex;gap:17px}
.about-cols .body-text{width:129px}

/* quote */
.quote-photo{position:absolute;inset:0;background:linear-gradient(180deg,#8ea1b8 0%,#7b8da5 35%,#5b6571 60%,#3d3f3d 82%,#6d6a64 100%)}
.quote{position:absolute;left:36px;top:72px;width:140px;text-align:center;font-size:6.3px;line-height:1.4}
.quote p{margin-bottom:7px}
.quote-mark{font-weight:800;font-size:40px;line-height:.6;font-style:normal}
.quote-open{position:absolute;left:32px;top:73px}
.quote-close{position:absolute;left:156px;top:208px}

/* construction */
.services .page-title{top:39px}
.service{position:absolute;left:38px;display:flex}
.service-icon{width:46px;height:46px;border-radius:50%;background:var(--white);display:flex;align-items:center;justify-content:center;flex:none}
.service-list{margin-left:16px}
.service-list h3{font-size:8.8px;font-weight:800;text-transform:uppercase;margin-bottom:1px;padding-left:14px}
.service-list ul{list-style:none;font-size:5.5px;line-height:1.44}
.service-list li::before{content:"» "}
</style>
</head>
<body>
<svg class="backdrop" viewBox="0 0 1200 1146" aria-hidden="true">
  <polygon points="1200,56 1200,1146 12,1146" fill="var(--bg-dark)"/>
</svg>

<!-- Cover -->
<section class="page cover col-1 row-1">
  <div class="cover-photo" role="img" aria-label="City skyline at sunset above parkland"></div>
  <h1 class="page-title">Capability<br>Statement</h1>
  <div class="brand"><span class="brand-square"></span>RIDGELINE PLUMBERS.</div>
</section>

<!-- Contents -->
<section class="page contents col-2 row-1">
  <h2 class="page-title">Table of<br>Contents</h2>
  <ol class="toc">
    <li>From the Directors<span class="dots"></span>3</li>
    <li>About the Business<span class="dots"></span>4</li>
    <li>Our Services<span class="dots"></span>6</li>
    <li>RP Data<span class="dots"></span>7</li>
    <li>Meet the Team<span class="dots"></span>8</li>
    <li>Recent Projects<span class="dots"></span>9</li>
    <li>RP Data<span class="dots"></span>10</li>
    <li>Meet the Team<span class="dots"></span>12</li>
  </ol>
  <div class="brand"><span class="brand-square"></span>RIDGELINE PLUMBERS.</div>
</section>

<!-- Introduction -->
<section class="page intro col-3 row-1">
  <h2 class="page-title">Introduction</h2>
  <div class="body-text">
    <p>Our modern day approach to Plumbing construction means that your Project benefits from the latest materials, techniques, and industry developments. As leaders in high quality construction Plumbing, commercial maintenance, and retail fit-outs, we stand at the forefront of Plumbing in Perth.</p>
    <p>Our innovative and dynamic approach to business places us ahead of our competition and showcases our skill and experience in delivering the right products and installation methods for your Projects. We work closely with our Builders on the scope of works, to guarantee that targets are met, and exceeded.</p>
    <div class="callout">Ridgeline Plumbers having extensive expertise across many areas,<br>from new Shopping centres and Hospitals to industrial equipment.</div>
    <p>We constantly strive to exceed the expectations of our Customers and have a proven track record with the delivery of large-scale Projects, on time and on budget, and firmly believe that it is our job to make your Project a success and your experience positive.</p>
    <p>We pride ourselves on having the highest level of quality on-site management in the industry, displaying expert communication, effective collaboration and unmatched problem solving skills. We stand steadfast upon our reputation as problem solvers and innovative and flexible service providers.</p>
    <p>Ridgeline Plumbers believe with the proper team, you can avoid costly and unnecessary delays. When you work with us, you know that you are dealing with Perth's most trusted specialists in commercial Plumbing.</p>
    <p>We can't wait to start working with you.</p>
  </div>
  <div class="brand"><span class="brand-square"></span>RIDGELINE PLUMBERS.</div>
</section>

<!-- About -->
<section class="page about col-1 row-2">
  <h2 class="page-title">About the<br>Business</h2>
  <div class="about-cols">
    <div class="body-text">
      <p>Established in February 2004 by Managing Directors Daniel Ferraro and Owen Hartley, Ridgeline Plumbers specialises in the commercial sector and has extensive expertise in all levels of the industry, from new Shopping centres, Hotels, high-rise developments and Hospitals to industrial equipment in both construction and maintenance.</p>
      <p>Our relationships with our Suppliers is paramount to the success of our business and we have trading accounts with all major Plumbing Suppliers in Perth. We maintain working relationships with Manufacturers to ensure that we are the forefront of advancements within the Plumbing industry, both in products and Plumbing techniques.</p>
      <p>We strive for a balance in cost-effective Plumbing, whilst keeping the highest standards in the industry. We are relentless in our pursuit of quality and excellence in service. Our approach is built on collaboration, innovation, integrity and accountability - which underpin every interaction at each stage of the work we do.</p>
      <p>We focus on the relationships we build with our Customers, Colleagues, and Stakeholders to ensure the best outcomes.</p>
    </div>
    <div class="body-text">
      <p>At Ridgeline Plumbers, we believe our excellent customer relations, passion about the industry and our expertise means we can deliver what we promise. We know this sets us apart as our satisfied Customers keep coming back, as well as recommending us to others and we believe this word of mouth speaks volumes.</p>
      <p>We know that our success, and success of our Projects, depends on the quality of our People. We are committed to attracting and retaining talented employees by providing a strong platform for ongoing career development. We recognise the value in every team member.</p>
      <p>We proudly employ a highly skilled team of full time staff ranging from fully qualified Trades people, Apprentices, and Administration Personnel. We are committed to the regular, ongoing training and cross-skilling of all our staff and promote a workplace culture that supports career advancement as well as professional and personal growth.</p>
    </div>
  </div>
  <div class="brand"><span class="brand-square"></span>RIDGELINE PLUMBERS.</div>
</section>

<!-- Quote -->
<section class="page quote-page col-2 row-2">
  <div class="quote-photo" role="img" aria-label="High-rise building under construction with tower cranes"></div>
  <span class="quote-mark quote-open">"</span>
  <blockquote class="quote">
    <p>As commercial Builders we often have to work on difficult Projects that require unique, innovative results.</p>
    <p>Ridgeline Plumbers are problem solvers and work closely with our team to deliver high quality solution oriented Projects. We started working with Ridgeline Plumbers several years ago and continue to be impressed by their professionalism and attention to detail.</p>
  </blockquote>
  <span class="quote-mark quote-close">"</span>
  <div class="brand"><span class="brand-square"></span>RIDGELINE PLUMBERS.</div>
</section>

<!-- Construction services -->
<section class="page services col-3 row-2">
  <h2 class="page-title">Construction</h2>

  <div class="service" style="top:90px">
    <div class="service-icon">
      <svg width="26" height="26" viewBox="0 0 26 26" fill="none" stroke="var(--navy)" stroke-width="1.4" aria-hidden="true">
        <rect x="4" y="5" width="11" height="18"/><rect x="15" y="11" width="7" height="12"/>
        <path d="M7 9h2M11 9h1M7 13h2M11 13h1M7 17h2M11 17h1M18 15h1M18 19h1M2 23h22"/>
      </svg>
    </div>
    <div class="service-list">
      <h3>Construction</h3>
      <ul>
        <li>Airports</li><li>Apartments / Mixed Use Developments</li><li>Commercial Fitouts</li><li>Defence &amp; Government</li><li>Education</li><li>Fire Services</li><li>Hotels</li><li>Health</li><li>HVAC - Cooling Towers</li><li>Multi Storey Office Blocks</li><li>Retail</li><li>Sporting / Recreation Facilities</li>
      </ul>
    </div>
  </div>

  <div class="service" style="top:206px">
    <div class="service-icon">
      <svg width="30" height="30" viewBox="0 0 30 30" aria-hidden="true">
        <circle cx="15" cy="15" r="9" fill="none" stroke="var(--navy)" stroke-width="5" stroke-dasharray="3.5 3.6"/>
        <circle cx="15" cy="15" r="7.5" fill="var(--navy)"/>
        <circle cx="15" cy="15" r="4" fill="var(--white)"/>
        <path d="M11 19l8-8" stroke="var(--navy)" stroke-width="2"/>
      </svg>
    </div>
    <div class="service-list">
      <h3>Maintenance</h3>
      <ul>
        <li>24/7 Assistance</li><li>Backflow Devices</li><li>Blocked Drains</li><li>Gas and Water Leaks</li><li>Hot Water Systems</li><li>Preventative Maintenance Programs</li><li>Pump Systems</li><li>Reactive</li><li>Roof Leaks</li><li>Servicing</li><li>Thermostatic Mixing Valves</li>
      </ul>
    </div>
  </div>

  <div class="service" style="top:313px">
    <div class="service-icon">
      <svg width="26" height="26" viewBox="0 0 26 26" fill="none" stroke="var(--navy)" stroke-width="1.4" aria-hidden="true">
        <rect x="3" y="3" width="20" height="20" rx="2"/>
        <path d="M3 11h8v-8M15 3v6h8M11 23v-7h5M16 16v7M19 16h4"/>
      </svg>
    </div>
    <div class="service-list">
      <h3>Surveying</h3>
      <ul>
        <li>Annual Testing</li><li>Audits</li><li>Budget Assistance</li><li>Capital Asset Reports</li><li>CCTV</li><li>Design Assistance</li><li>Pipe Locating</li><li>Pipework Surveying</li><li>Preliminary Investigations</li><li>Water Saving</li>
      </ul>
    </div>
  </div>

  <div class="brand"><span class="brand-square"></span>RIDGELINE PLUMBERS.</div>
</section>
</body>
</html>
```